The Bright Socket Business cards

one side I would like my logo (uploaded) and the other side I want my details. I'm an electrician in sydney. The logo side I'm happy with just a white background and our logo in the middle.

Details for other side
24/7 Sydney Electrician
Marcus Hale
0431 758 216
marcus@thebrightsocket.com.au
thebrightsocket.com.au
icons for facebook, instagram, linked in

electrician

company info

```html
<!DOCTYPE html>
<html lang="en">
<head>
<meta charset="utf-8">
<title>The Bright Socket – Business Cards</title>
<link href="https://fonts.googleapis.com/css2?family=Lexend:wght@400;500;600&display=swap" rel="stylesheet">
<style>
  :root {
    --backdrop: #232323;
    --card: #0d0d0d;
    --brand-red: #ee3524;
    --ink-light: #f4f4f4;
  }
  * { box-sizing: border-box; margin: 0; padding: 0; }
  html, body { width: 1200px; height: 901px; overflow: hidden; }
  body {
    background: var(--backdrop);
    position: relative;
    font-family: "Lexend", sans-serif;
  }
  .card {
    position: absolute;
    top: 316px;
    width: 471px;
    height: 269px;
    background: var(--card);
    border-radius: 10px;
    overflow: hidden;
  }
  .card--details { left: 116px; }
  .card--brand { left: 613px; }

  .wordmark {
    position: absolute;
    color: var(--brand-red);
    font-weight: 600;
    font-size: 25px;
    line-height: 1.05;
    letter-spacing: 0.06em;
    text-transform: uppercase;
  }
  .card--details .wordmark { left: 26px; top: 26px; }
  .card--brand .wordmark { right: 26px; bottom: 22px; text-align: right; }

  .brand-disc {
    position: absolute;
    border-radius: 50%;
    background: var(--brand-red);
  }
  .card--details .brand-disc { left: 272px; top: 47px; width: 176px; height: 176px; }
  .card--brand .brand-disc { left: 25px; top: 46px; width: 174px; height: 174px; }

  .person {
    position: absolute;
    left: 25px;
    top: 135px;
  }
  .person__name {
    color: var(--brand-red);
    font-weight: 500;
    font-size: 18px;
    letter-spacing: 0.01em;
    text-transform: uppercase;
  }
  .person__role {
    color: var(--ink-light);
    font-size: 13px;
    margin-top: 2px;
  }
  .contact {
    position: absolute;
    left: 25px;
    top: 191px;
    list-style: none;
  }
  .contact__item {
    display: flex;
    align-items: center;
    gap: 7px;
    color: var(--ink-light);
    font-size: 13.5px;
    height: 19.5px;
  }
  .contact__icon { width: 13px; height: 13px; flex: none; }

  .socials {
    position: absolute;
    right: 26px;
    top: 25px;
    display: flex;
    gap: 10px;
    list-style: none;
  }
  .socials__dot {
    width: 18px;
    height: 18px;
    border-radius: 50%;
    background: var(--brand-red);
  }
</style>
</head>
<body>
  <section class="card card--details" aria-label="Business card, details side">
    <div class="wordmark">The Bright<br>Socket</div>

    <div class="person">
      <p class="person__name">Marcus Hale</p>
      <p class="person__role">24/7 Sydney Electrician</p>
    </div>

    <ul class="contact">
      <li class="contact__item">
        <svg class="contact__icon" viewBox="0 0 24 24" aria-hidden="true"><path fill="#ee3524" d="M6.6 10.8a15.1 15.1 0 0 0 6.6 6.6l2.2-2.2c.3-.3.7-.4 1-.2 1.1.4 2.3.6 3.6.6.6 0 1 .4 1 1V20c0 .6-.4 1-1 1A17 17 0 0 1 3 4c0-.6.4-1 1-1h3.5c.6 0 1 .4 1 1 0 1.3.2 2.5.6 3.6.1.3 0 .7-.2 1z"/></svg>
        0431 758 216
      </li>
      <li class="contact__item">
        <svg class="contact__icon" viewBox="0 0 24 24" aria-hidden="true"><path fill="#ee3524" d="M2 5h20v14H2z"/><path fill="none" stroke="#0d0d0d" stroke-width="2" d="M2 6l10 7 10-7"/></svg>
        marcus@thebrightsocket.com.au
      </li>
      <li class="contact__item">
        <svg class="contact__icon" viewBox="0 0 24 24" aria-hidden="true"><g fill="none" stroke="#ee3524" stroke-width="2"><circle cx="12" cy="12" r="10"/><ellipse cx="12" cy="12" rx="4.5" ry="10"/><path d="M2 12h20M4 6.5h16M4 17.5h16"/></g></svg>
        thebrightsocket.com.au
      </li>
    </ul>

    <div class="brand-disc" aria-hidden="true"></div>
  </section>

  <section class="card card--brand" aria-label="Business card, brand side">
    <div class="brand-disc" aria-hidden="true"></div>

    <ul class="socials" aria-label="Social profile links">
      <li class="socials__dot" aria-hidden="true"></li>
      <li class="socials__dot" aria-hidden="true"></li>
      <li class="socials__dot" aria-hidden="true"></li>
    </ul>

    <div class="wordmark">The Bright<br>Socket</div>
  </section>
</body>
</html>
```